Custom Home Builder Needs a Website

Harbor Stone Builders Ltd. requires a clean professional 5 page website - Home, About Us, Gallery (Interior and Exterior), Our Process and Contact Us(with registration form). We are a home builder who also has homes for sale. Also please have a place for video embedding. Editable fields by user. Using the stationery 'feel' that is attached. Need social media links. If you require any additional files, please request.

Target Market(s)

Families and professionals

Industry/Entity Type

Home Builder

Coding

Coded - Design and coding required

Number of Pages Required

5+ page

Font styles to use
Sans Serif
Other font styles liked:
• Lato

Requirements
Must have
• Editable by user
• Register Button
• Place to put home models for sale - preferably on the first page
• 5 page website -
• -Home
• -About Us
• -Gallery (Interior and Exterior)
• -Our Process
• -Contact Us.
Nice to have
• Themed similar to current stationery
• place for video embedding
• Try some darker backgrounds
• Change pictures to B/W if works for design
Should not have
• cartoonish type of content

```html
<!DOCTYPE html>
<html lang="en">
<head>
<meta charset="utf-8">
<title>Harbor Stone Builders Ltd.</title>
<link rel="stylesheet" href="https://fonts.googleapis.com/css2?family=Lato:wght@400;700;900&display=swap">
<style>
:root{
  --green:#6cb33f;
  --green-light:#86c440;
  --green-dark:#1f3a2a;
  --green-deep:#14271c;
  --ink:#2b2b2b;
  --text:#555;
  --grey:#bdbdbd;
  --white:#fff;
}
*{box-sizing:border-box;margin:0;padding:0}
html,body{width:1200px;height:3579px;overflow:hidden}
body{font-family:'Lato',sans-serif;color:var(--text);background:var(--white);position:relative}
.abs{position:absolute}
.section-title{position:absolute;left:0;width:1200px;text-align:center;font-size:28px;font-weight:400;text-transform:uppercase;letter-spacing:.5px}
.section-title::after{content:"";display:block;width:90px;height:2px;background:currentColor;opacity:.5;margin:12px auto 0}

/* header */
.site-header{position:absolute;top:0;left:0;width:1200px;height:100px;background:var(--white);box-shadow:0 2px 8px rgba(0,0,0,.12);z-index:2}
.brand{position:absolute;left:79px;top:22px}
.brand-name{font-size:21px;font-weight:900;color:var(--green-dark);letter-spacing:.5px;text-transform:uppercase;line-height:1}
.brand-tag{margin-top:9px;font-size:10px;letter-spacing:9px;color:#777;text-transform:uppercase}
.main-nav{position:absolute;left:525px;top:41px;display:flex;gap:18px;font-size:14px;font-weight:700;color:var(--ink);text-transform:uppercase}
.register-btn{position:absolute;left:964px;top:29px;width:155px;height:40px;background:var(--green);color:var(--white);font-size:12px;font-weight:700;text-transform:uppercase;display:flex;align-items:center;padding-left:48px;border-radius:2px}
.register-btn svg{position:absolute;left:12px;top:9px}

/* hero */
.hero{position:absolute;top:100px;left:0;width:1200px;height:568px;background:linear-gradient(180deg,#c9d0d6 0%,#8f969b 35%,#4f5559 70%,#6f7a5f 100%)}
.hero-band{position:absolute;left:296px;top:246px;width:610px;height:70px;background:rgba(20,20,20,.55);color:var(--white);font-size:31px;font-weight:900;text-align:center;line-height:70px;text-transform:uppercase}

/* welcome */
.welcome-title{position:absolute;left:79px;top:736px;font-size:26px;color:var(--ink);text-transform:uppercase}
.welcome-title::after{content:"";display:block;width:560px;height:1px;background:#999;margin-top:10px}
.welcome-copy{position:absolute;left:79px;top:806px;width:600px;font-size:12.5px;line-height:20px;color:#555}
.welcome-copy p+p{margin-top:20px}
.video{position:absolute;left:723px;top:811px;width:334px;height:232px;background:linear-gradient(180deg,#9fb8d6 0%,#c9d3de 50%,#a59b7e 100%)}
.video-bar{position:absolute;left:0;bottom:0;width:334px;height:24px;background:#e4e4e4;border-top:1px solid #bbb}

/* services */
.services{position:absolute;top:1110px;left:0;width:1200px;height:541px;background:linear-gradient(180deg,#4a6a55 0%,#2c4d38 55%,#1c3526 100%)}
.service{position:absolute;top:155px;width:241px;text-align:center}
.service-photo{width:241px;height:190px}
.service h3{margin-top:34px;font-size:15px;font-weight:700;color:var(--green-light);text-transform:uppercase}
.service p{margin:10px auto 0;width:220px;font-size:11px;line-height:16px;color:var(--white);font-weight:700}

/* process */
.step{position:absolute;top:1821px;width:200px;text-align:center}
.step-icon{width:100px;height:100px;border-radius:50%;background:var(--grey);margin:0 auto;display:flex;align-items:center;justify-content:center}
.step h3{margin-top:30px;font-size:15px;color:var(--green);font-weight:700;text-transform:uppercase}
.step p{margin:10px auto 0;width:170px;font-size:11px;line-height:16px;color:#666}

/* testimonial */
.testimonial{position:absolute;top:2095px;left:0;width:1200px;height:489px;background:linear-gradient(180deg,#a8c63c 0%,#84b83b 50%,#5da63c 100%)}
.quote{position:absolute;top:276px;left:240px;width:720px;text-align:center;font-size:18px;line-height:29px;color:#2a3a1e}
.quote-name{position:absolute;top:386px;left:0;width:1200px;text-align:center;font-size:11px;color:#2a3a1e;text-transform:uppercase}
.quote-place{position:absolute;top:408px;left:0;width:1200px;text-align:center;font-size:11px;color:#2a3a1e}

/* properties */
.property{position:absolute;top:2741px;width:329px}
.property-photo{width:329px;height:211px}
.property-label{height:66px;background:var(--green);color:var(--white);text-align:center;padding-top:13px}
.property-label strong{display:block;font-size:18px;font-weight:700}
.property-label span{display:block;margin-top:3px;font-size:11px}
.all-homes{position:absolute;left:522px;top:3080px;width:156px;height:36px;background:var(--green-dark);color:var(--white);font-size:12px;text-align:center;line-height:36px;text-transform:uppercase;border-radius:2px}

/* footer */
.site-footer{position:absolute;top:3185px;left:0;width:1200px;height:334px;background:linear-gradient(180deg,#2c4a38 0%,#1f3a2a 60%,#1a3124 100%)}
.footer-heading{position:absolute;top:66px;font-size:14px;color:var(--green-light);text-transform:uppercase;font-weight:700}
.quick-links{position:absolute;left:79px;top:118px;list-style:none;font-size:12px;line-height:24px;color:var(--white);text-transform:uppercase}
.quick-links li::before{content:"» "}
.mission-photo{position:absolute;left:329px;top:115px;width:131px;height:138px;border:3px solid var(--white);background:linear-gradient(180deg,#b8a898,#7d6a5c)}
.mission-copy{position:absolute;left:475px;top:113px;width:305px;font-size:11.5px;line-height:20px;color:var(--white)}
.contact-row{position:absolute;left:792px;font-size:12px;color:var(--white);display:flex;align-items:center;gap:12px}
.social{position:absolute;left:818px;top:3414px;display:flex;gap:16px}
.social span{width:26px;height:26px;border-radius:3px;background:#3f8fcf}
.copyright{position:absolute;top:3519px;left:0;width:1200px;height:60px;background:var(--green-deep);color:#c9c9c9;font-size:10px;text-align:center;line-height:60px;text-transform:uppercase;letter-spacing:.3px}
</style>
</head>
<body>

<header class="site-header">
  <div class="brand">
    <div class="brand-name">Harbor Stone Builders Ltd.</div>
    <div class="brand-tag">Design · Build</div>
  </div>
  <nav class="main-nav"><span>Home</span><span>About</span><span>Services</span><span>Process</span><span>Gallery</span><span>Contact</span></nav>
  <div class="register-btn">
    <svg width="22" height="22" viewBox="0 0 22 22"><circle cx="11" cy="11" r="9" fill="none" stroke="#fff" stroke-width="2"/><path d="M7 11l3 3 5-6" fill="none" stroke="#fff" stroke-width="2"/></svg>
    Register Now
  </div>
</header>

<section class="hero" role="img" aria-label="Two-storey craftsman home with stone base and double garage under a cloudy sky">
  <div class="hero-band">Designed to Preform, Built to Last</div>
</section>

<section class="welcome">
  <h1 class="welcome-title" style="font-weight:400">Welcome to Harbor Stone Builders Ltd.</h1>
  <div class="welcome-copy">
    <p>Lorem ipsum dolor sit amet, consectetur adipiscing elit. Morbi eu ligula sit amet elit consectetur iaculis sit amet eu velit. Sed tempus leo felis, quis mollis velit euismod sed. Fusce porttitor sagittis est. Nam consectetur porta euismod. Nulla rhoncus, nisi non efficitur lacinia, metus risus efficitur lacus, sit amet ornare magna tellus volutpat mi. Quisque scelerisque dui non tincidunt tempor.</p>
    <p>Cras egestas lectus urna, quis interdum nulla aliquam eu. Vestibulum lobortis sem sed tortor lacinia, id aliquet turpis hendrerit. Curabitur tempus non risus nec dictum. Mauris vel pharetra sapien, a consectetur velit. In hac habitasse platea dictumst. In odio metus, scelerisque ac odio id, lobortis porttitor turpis. Fusce vel diam quis nunc dignissim dignissim nec et sem. Nulla ut ligula tristique, bibendum libero ac, tempor diam. Sed vitae risus nec diam aliquam mollis. Nulla condimentum nunc sed posuere aliquam. Mauris vel efficitur lacus. Ut a risus risus. Duis sed sodales dui.</p>
  </div>
  <div class="video" role="img" aria-label="Welcome video of the builder standing in an open prairie field">
    <div class="video-bar">
      <svg width="334" height="24" viewBox="0 0 334 24">
        <path d="M10 6l9 6-9 6z" fill="#555"/>
        <rect x="30" y="10" width="200" height="4" rx="2" fill="#aaa"/>
        <text x="245" y="16" font-family="Lato, sans-serif" font-size="9" fill="#444">0:00 / 0:00</text>
        <path d="M300 9h4l5-4v14l-5-4h-4z" fill="#555"/>
        <rect x="315" y="7" width="12" height="10" fill="none" stroke="#555" stroke-width="1.5"/>
      </svg>
    </div>
  </div>
</section>

<section class="services" aria-label="Our services">
  <h2 class="section-title" style="top:58px;color:var(--white)">Our Services</h2>
  <div class="service" style="left:79px">
    <div class="service-photo" role="img" aria-label="Couple embracing in front of a new home" style="background:linear-gradient(180deg,#3f77c4,#9cc3e6 55%,#5f8f3a)"></div>
    <h3>New Home Construction</h3>
    <p>Lorem ipsum dolor sit amet, consectetur adipiscing elit. Etiam facilisis tempor eget purus efficitur ut.</p>
  </div>
  <div class="service" style="left:346px">
    <div class="service-photo" role="img" aria-label="Surveyor with camera looking over land at sunset" style="background:linear-gradient(180deg,#f3c28a,#e08a4e 50%,#5a3a2a)"></div>
    <h3>Land Development</h3>
    <p>Lorem ipsum dolor sit amet, consectetur adipiscing elit. Etiam facilisis tempor eget purus efficitur ut.</p>
  </div>
  <div class="service" style="left:613px">
    <div class="service-photo" role="img" aria-label="Workers in hard hats renovating an interior" style="background:linear-gradient(180deg,#c99a6a,#8a6440 55%,#d8c23a)"></div>
    <h3>Renovations</h3>
    <p>Lorem ipsum dolor sit amet, consectetur adipiscing elit. Etiam facilisis tempor eget purus efficitur ut.</p>
  </div>
  <div class="service" style="left:880px">
    <div class="service-photo" role="img" aria-label="Team joining puzzle pieces on a table" style="background:linear-gradient(180deg,#5d6166,#8e9397 50%,#46494d)"></div>
    <h3>Consulting/Partnerships</h3>
    <p>Lorem ipsum dolor sit amet, consectetur adipiscing elit. Etiam facilisis tempor eget purus efficitur ut.</p>
  </div>
</section>

<section class="process" aria-label="Our process">
  <h2 class="section-title" style="top:1705px;color:var(--ink)">Our Process</h2>
  <div class="step" style="left:69px">
    <div class="step-icon"><svg width="54" height="54" viewBox="0 0 54 54"><path d="M14 38a10 10 0 0 1 1-20 13 13 0 0 1 25 3 8 8 0 0 1 0 17z" fill="#fff"/><path d="M20 30l7-6 7 6v7H20z" fill="#bdbdbd"/></svg></div>
    <h3>The Dream</h3>
    <p>Pellentesque ultrices porta ipsum. Cum sociis natoque penatib nascetur ridiculus.</p>
  </div>
  <div class="step" style="left:284px">
    <div class="step-icon"><svg width="54" height="54" viewBox="0 0 54 54"><path d="M14 40L38 16M18 44l-6 2 2-6" stroke="#fff" stroke-width="4" fill="none"/><path d="M14 14l26 26" stroke="#fff" stroke-width="6"/></svg></div>
    <h3>The Design</h3>
    <p>Pellentesque ultrices porta ipsum. Cum sociis natoque penatib nascetur ridiculus.</p>
  </div>
  <div class="step" style="left:497px">
    <div class="step-icon"><svg width="54" height="54" viewBox="0 0 54 54"><path d="M14 40l16-16" stroke="#fff" stroke-width="6" stroke-linecap="round"/><circle cx="34" cy="20" r="8" fill="none" stroke="#fff" stroke-width="5"/><path d="M40 40L20 20" stroke="#fff" stroke-width="4"/></svg></div>
    <h3>The Build</h3>
    <p>Pellentesque ultrices porta ipsum. Cum sociis natoque penatib nascetur ridiculus.</p>
  </div>
  <div class="step" style="left:706px">
    <div class="step-icon"><svg width="54" height="54" viewBox="0 0 54 54"><path d="M27 8v38M8 27h38" stroke="#fff" stroke-width="3"/><path d="M27 6l-5 6h10zM27 48l-5-6h10zM6 27l6-5v10zM48 27l-6-5v10z" fill="#fff"/></svg></div>
    <h3>The Move</h3>
    <p>Pellentesque ultrices porta ipsum. Cum sociis natoque penatib nascetur ridiculus.</p>
  </div>
  <div class="step" style="left:919px">
    <div class="step-icon"><svg width="54" height="54" viewBox="0 0 54 54"><circle cx="27" cy="22" r="13" fill="none" stroke="#fff" stroke-width="4"/><path d="M27 15l2 5h5l-4 3 2 5-5-3-5 3 2-5-4-3h5z" fill="#fff"/><path d="M20 33l-4 14 6-3 4 5 2-13M34 33l4 14-6-3-4 5" fill="#fff"/></svg></div>
    <h3>Warranty and Beyond</h3>
    <p>Pellentesque ultrices porta ipsum. Cum sociis natoque penatib nascetur ridiculus.</p>
  </div>
</section>

<section class="testimonial" aria-label="Testimonial">
  <h2 class="section-title" style="top:58px;color:var(--white)">Testimonial</h2>
  <svg class="abs" style="left:420px;top:153px" width="360" height="80" viewBox="0 0 360 80">
    <line x1="12" y1="40" x2="348" y2="40" stroke="#2a3a1e" stroke-width="1.5"/>
    <rect x="6" y="34" width="12" height="12" fill="#1f3a2a"/>
    <rect x="342" y="34" width="12" height="12" fill="#1f3a2a"/>
    <circle cx="180" cy="40" r="37" fill="#fff"/>
    <circle cx="180" cy="40" r="33" fill="#a08a78" role="img" aria-label="Client portrait"/>
  </svg>
  <p class="quote">Curabitur viverra dolor id lacinia euismod. In lacinia felis sed nisi aliquam commodo id in dui pellentesque faucibus lacus eget interdum molestie. Suspendisse ac lacinia erat.</p>
  <div class="quote-name">Dana Whitfield</div>
  <div class="quote-place">Portland, OR</div>
</section>

<section class="properties" aria-label="Our properties">
  <h2 class="section-title" style="top:2638px;color:var(--ink)">Our Properties</h2>
  <div class="property" style="left:79px">
    <div class="property-photo" role="img" aria-label="Two-storey home with stone columns" style="background:linear-gradient(180deg,#e9edf0,#6d6a66 55%,#4f4a44)"></div>
    <div class="property-label"><strong>Move In Special-1/2 Off 1st Month!!</strong><span>View Details&gt;&gt;</span></div>
  </div>
  <div class="property" style="left:434px">
    <div class="property-photo" role="img" aria-label="Grey craftsman home at dusk" style="background:linear-gradient(180deg,#d6dde4,#4d5258 55%,#3b3f44)"></div>
    <div class="property-label"><strong>Beautiful Lakeside Home for Sale!</strong><span>View Details&gt;&gt;</span></div>
  </div>
  <div class="property" style="left:790px">
    <div class="property-photo" role="img" aria-label="Large home with two garages and stone trim" style="background:linear-gradient(180deg,#f1f1ef,#8a8680 55%,#6a665f)"></div>
    <div class="property-label"><strong>$200 Off 1st Months Booking!!</strong><span>View Details&gt;&gt;</span></div>
  </div>
  <div class="all-homes">View All Homes</div>
</section>

<footer class="site-footer">
  <div class="footer-heading" style="left:79px">Quick Links</div>
  <div class="footer-heading" style="left:327px">Our Mission</div>
  <div class="footer-heading" style="left:792px">Contact Us</div>
  <ul class="quick-links">
    <li>Home</li><li>About Us</li><li>Our Services</li><li>Our Process</li><li>Gallery</li><li>Contact Us</li>
  </ul>
  <div class="mission-photo" role="img" aria-label="Portrait of the company owner"></div>
  <p class="mission-copy">Our projects start with a vision, with a priority to build attractive, appealing and functional homes. To build the home that suits you best, we will spend time getting to know you and your family, with your specific wants and needs. Our goal is to put the same thought and care in every project that we would put into our own home.</p>
  <div class="contact-row" style="top:114px"><svg width="14" height="16" viewBox="0 0 14 16"><path d="M7 0a6 6 0 0 0-6 6c0 4 6 10 6 10s6-6 6-10a6 6 0 0 0-6-6z" fill="#fff"/><circle cx="7" cy="6" r="2" fill="#1f3a2a"/></svg>PO Box 208 Fairview, SK, S0K 2B0</div>
  <div class="contact-row" style="top:150px"><svg width="14" height="16" viewBox="0 0 14 16"><path d="M3 1l3 3-2 2c1 2 3 4 5 5l2-2 3 3-2 3C6 15 0 9 1 3z" fill="#fff"/></svg>306 555 0142</div>
  <div class="contact-row" style="top:186px"><svg width="14" height="12" viewBox="0 0 14 12"><rect x="0" y="1" width="14" height="10" fill="#fff"/><path d="M0 1l7 6 7-6" fill="none" stroke="#1f3a2a" stroke-width="1.2"/></svg>info@harborstonebuilders.com</div>
</footer>
<div class="social" aria-label="Social media links"><span></span><span></span><span></span><span></span></div>
<div class="copyright">Copyright© 2017 info@harborstonebuilders.com. All rights are reserved.</div>

</body>
</html>
```